Business Card Design Project

Beauty Therapist
Bold, bright, feminine, like contrast, love flowers, girly stuff. Must be beautiful. But open to all suggestions. Business name: Plucky Plum.
xxx
Dorota Kaczmarczyk
Updates

Project Deadline Extended
Reason: I think you need more time to design something good. X

Target Market(s)

ignore this

Industry/Entity Type

Business

```html
<!DOCTYPE html>
<html lang="en">
<head>
<meta charset="utf-8">
<title>Plucky Plum – Business Card</title>
<link rel="stylesheet" href="https://fonts.googleapis.com/css2?family=Dancing+Script:wght@700&family=Quicksand:wght@400&display=swap">
<style>
  :root {
    --stage: #4a4a4a;
    --card-pink: #f6d3ea;
    --card-light: #fdf3f9;
    --magenta: #e5087f;
    --ink: #1d1a1c;
    --petal-lilac: #b57fc6;
    --petal-cream: #fbe9cf;
    --leaf: #3c9e6e;
  }
  html, body {
    margin: 0;
    width: 1027px;
    height: 1200px;
    overflow: hidden;
    background: var(--stage);
  }
  .card {
    position: absolute;
    left: 33px;
    width: 960px;
    height: 553px;
    overflow: hidden;
    background:
      radial-gradient(ellipse 60% 70% at 30% 45%, var(--card-light) 0%, rgba(253,243,249,0) 70%),
      linear-gradient(180deg, var(--card-pink) 0%, #fbe6f3 55%, var(--card-pink) 100%);
    box-shadow: 0 4px 10px rgba(0,0,0,0.55);
  }
  .card--front { top: 28px; }
  .card--back  { top: 611px; }

  .floral {
    position: absolute;
    display: block;
  }
  .card--front .floral { left: 400px; top: 40px; width: 560px; height: 513px; }
  .card--back  .floral { left: 0; top: 40px; width: 580px; height: 513px; }

  .script {
    position: absolute;
    margin: 0;
    font-family: "Dancing Script", cursive;
    font-weight: 700;
    color: var(--magenta);
    line-height: 1;
    white-space: nowrap;
  }
  .caps {
    position: absolute;
    margin: 0;
    font-family: "Quicksand", sans-serif;
    font-weight: 400;
    color: var(--ink);
    text-transform: uppercase;
    line-height: 1;
    white-space: nowrap;
  }

  .front-brand   { left: 80px; top: 82px; font-size: 128px; }
  .front-role    { left: 84px; top: 245px; font-size: 50px; letter-spacing: 3px; }

  .back-name     { right: 34px; top: 86px; font-size: 84px; }
  .back-role     { right: 34px; top: 180px; font-size: 37px; letter-spacing: 3px; }
  .back-phone    { right: 34px; top: 236px; font-size: 72px; }
  .back-brand    { right: 34px; top: 412px; font-size: 90px; }
</style>
</head>
<body>

<section class="card card--front">
  <svg class="floral" role="img" aria-label="Illustration of lilac and cream flowers with green leaves" viewBox="0 0 560 513">
    <defs>
      <radialGradient id="floralFront" cx="0.62" cy="0.62" r="0.6">
        <stop offset="0" stop-color="var(--petal-cream)"/>
        <stop offset="0.55" stop-color="#e9c6e6"/>
        <stop offset="1" stop-color="#f6d3ea" stop-opacity="0"/>
      </radialGradient>
    </defs>
    <rect width="560" height="513" fill="url(#floralFront)"/>
  </svg>
  <p class="script front-brand">Plucky Plum</p>
  <p class="caps front-role">Beauty Therapist</p>
</section>

<section class="card card--back">
  <svg class="floral" role="img" aria-label="Illustration of lilac and cream flowers with green leaves" viewBox="0 0 580 513">
    <defs>
      <radialGradient id="floralBack" cx="0.35" cy="0.6" r="0.6">
        <stop offset="0" stop-color="var(--petal-cream)"/>
        <stop offset="0.55" stop-color="#e9c6e6"/>
        <stop offset="1" stop-color="#f6d3ea" stop-opacity="0"/>
      </radialGradient>
    </defs>
    <rect width="580" height="513" fill="url(#floralBack)"/>
  </svg>
  <p class="script back-name">Dorota Kaczmarczyk</p>
  <p class="caps back-role">Beauty Therapist</p>
  <p class="script back-phone">020 7946 0321</p>
  <p class="script back-brand">Plucky Plum</p>
</section>

</body>
</html>
```